Marvela Oil & Gas Exploation and Production Company Website

Need a website for an independent Oil and Gas Company. Want the design to be Conservative, Professional and Traditional Feeling. Use colors from Logo or soft tones. See Doc for thoughts on layout.

Not sure why this is showing desgins due. Try to work with QP to extend a couple days.

Target Market(s)

Mineral Owners, Investors, Potential Employees, Services Partners

Industry/Entity Type

Oil & Gas Exlploration and Production

Coding

Coded - Design and coding required

Number of Pages Required

5+ page

Colors
0054AA
0677BA
7BADD7
CADEEF
E8F1F8

Requirements
Must have
• Use best picture of rigs or landscape as you see fit, do nto have to use all picuters
Nice to have
• You can look at traditional Website for Portfolio companies exmaples at https://www.halvorcapital.example/about/upstream/portfolio, or https://brisonpower.example/our-portfolio/

```html
<!DOCTYPE html>
<html lang="en">
<head>
<meta charset="utf-8">
<title>Marvela Oil &amp; Gas</title>
<link href="https://fonts.googleapis.com/css2?family=Oswald:wght@400;500&family=Outfit:wght@300;400;500;600&display=swap" rel="stylesheet">
<style>
:root{
  --blue:#0054aa;
  --blue-band:#1557a8;
  --blue-mid:#0677ba;
  --ink:#111;
  --grey:#666;
  --pale:#eef2f8;
  --pale-2:#f3f5fa;
  --white:#fff;
  --line:#d6d9de;
  --oil:#b5dd9f;
  --wet:#fdf3d6;
  --dry:#f9b99a;
}
*{box-sizing:border-box;margin:0;padding:0}
html,body{width:1200px;height:4161px;overflow:hidden;background:var(--white)}
body{font-family:"Outfit",sans-serif;color:var(--ink)}
section,header{position:relative;width:1200px}
.abs{position:absolute}
.heading{font-family:"Oswald",sans-serif;font-weight:500;font-size:46px;letter-spacing:-0.5px;line-height:1;text-transform:uppercase}
.heading span{color:var(--blue)}
.center{left:0;right:0;text-align:center}

/* hero */
.hero{height:688px;background:linear-gradient(180deg,#b7b49a 0%,#d7c07a 30%,#e9b545 48%,#a99a43 62%,#5f7a2a 78%,#6f8a2a 100%)}
.brand{left:116px;top:38px;font-weight:600;font-size:38px;color:var(--blue);letter-spacing:1px}
.nav{right:121px;top:54px;display:flex;gap:31px;font-family:"Oswald",sans-serif;font-size:14px;color:#111;text-transform:uppercase}
.hero-card{left:549px;top:237px;width:530px;height:224px;background:rgba(160,140,80,.82);padding:18px 22px;color:var(--white)}
.hero-card h1{font-weight:600;font-size:35px;line-height:1.2;margin-bottom:8px}
.hero-card p{font-size:21px;line-height:1.55;font-weight:400}

/* about */
.about{height:499px}
.about .heading{left:116px;top:80px}
.about .lead{left:116px;top:150px;width:565px;font-weight:600;font-size:18px;line-height:1.6}
.about .body{left:116px;top:250px;width:570px;font-size:18.5px;line-height:1.42;color:var(--grey);font-weight:300}
.about-photo{left:740px;top:70px;width:340px;height:350px;border-radius:50%;background:radial-gradient(circle at 40% 40%,#c6d24c,#6f9a3a 60%,#3f6a2a)}

/* operations */
.ops{height:525px;background:var(--pale)}
.ops .heading{left:113px;top:60px}
.ops .lead{left:116px;top:122px;width:400px;font-weight:600;font-size:16px;line-height:1.8}
.legend{left:116px;top:265px;width:243px;height:215px;background:var(--white);border:1px solid var(--line);padding:12px 17px;font-size:19px}
.legend h3{font-weight:600;font-size:19px;margin-bottom:8px}
.legend li{list-style:none;display:flex;align-items:center;gap:12px;height:35px}
.legend i{width:34px;height:17px;display:block}
.scale{margin-top:12px;display:flex;align-items:center;gap:10px;font-size:11px}
.scale b{width:80px;height:9px;border:1px solid #333;display:block}
.ops-map{left:622px;top:21px;width:452px;height:488px;border:1px solid #c9ccd2;
  background:linear-gradient(105deg,var(--white) 0%,#f7f7f7 62%,var(--oil) 70%,var(--oil) 80%,var(--wet) 85%,var(--wet) 89%,var(--dry) 93%,var(--dry) 100%)}

/* related */
.related{height:307px;background:var(--blue-band)}
.related .heading{color:var(--white);top:58px}
.entity{top:146px;width:234px;height:100px;background:var(--white);border:2px solid #cfd8e6;padding:8px 12px;text-align:right}
.entity .mark{display:block;text-align:left;font-weight:600;font-size:38px;color:var(--blue);line-height:1.1;letter-spacing:1px}
.entity .sub{font-size:19px;color:#555}

/* management */
.team{height:622px}
.team .heading{top:90px}
.person{top:164px;width:304px;height:376px;border:1px solid var(--line);text-align:center;padding:7px}
.person .photo{height:290px;background:linear-gradient(180deg,#5d7595,#3a4b66 60%,#222a36)}
.person h3{font-family:"Oswald",sans-serif;font-weight:500;font-size:30px;color:var(--blue);margin-top:8px;line-height:1.2}
.person p{font-size:19px;color:#444}

/* news */
.news{height:743px;background:var(--pale-2)}
.news .heading{top:74px}
.story{top:147px;width:304px;text-align:center}
.story .photo{height:405px;border:1px solid var(--line);background:var(--white);padding:7px}
.story .photo div{height:100%}
.story h3{font-family:"Oswald",sans-serif;font-weight:400;font-size:30px;line-height:1.2;margin-top:22px}
.story time{display:block;font-size:19px;color:var(--blue);letter-spacing:1px;margin-top:6px}

/* contact */
.contact{height:777px}
.contact .heading{top:54px}
.directions{left:113px;top:139px;width:520px;height:543px;background:var(--pale-2);padding:40px 45px}
.directions h3{font-family:"Oswald",sans-serif;font-weight:500;font-size:34px;color:var(--blue);margin-bottom:38px}
.directions h4{font-weight:400;font-size:23px;margin-bottom:10px}
.directions p{font-size:18px;line-height:1.65;color:#333;font-weight:300;margin-bottom:44px}
.directions small{position:absolute;left:45px;bottom:20px;font-size:16px}
.form{left:654px;top:139px;width:426px;height:543px;background:linear-gradient(180deg,#1f4f8f,#1c4f95 60%,#2b5ea0);padding:22px 30px;color:var(--white);text-align:center}
.form h3{font-family:"Oswald",sans-serif;font-weight:500;font-size:34px;line-height:1.1}
.form .note{font-size:14px;margin:8px 0 16px}
.field{display:block;width:100%;height:55px;background:var(--white);border:0;margin-bottom:16px;font-family:"Outfit",sans-serif;font-size:17px;color:#999;text-align:left;padding:0 12px;font-weight:300}
textarea.field{height:127px;padding-top:14px;resize:none}
.submit{position:absolute;right:30px;bottom:28px;width:150px;height:55px;background:var(--blue-mid);border:2px solid #2f8ed6;color:var(--white);font-family:"Outfit",sans-serif;font-size:22px}
</style>
</head>
<body>

<header class="hero">
  <div class="abs" role="img" aria-label="Drilling rig standing in a green field at sunset" style="inset:0"></div>
  <div class="abs brand">MARVELA</div>
  <nav class="abs nav"><span>Home</span><span>About</span><span>Operations</span><span>Related Entities</span><span>News</span><span>Management</span><span>Contact</span></nav>
  <div class="abs hero-card">
    <h1>Experienced Upstream<br>Oil &amp; Gas Company</h1>
    <p>We focused a lease and drill development strategy that quickly brings cash returns to its investors and royalty owners.</p>
  </div>
</header>

<section class="about">
  <h2 class="abs heading">About <span>Marvela</span></h2>
  <p class="abs lead">Marvela Oil &amp; Gas, LLC was formed to pursue upstream acquisition and development opportunities in January 2022 by Grant Ellison and Victor Renaldi.</p>
  <p class="abs body">Marvela is focused on “Lease and Drill” opportunities in Unconventional Reservoirs.&nbsp; Marvela is also evaluating opportunities with existing production (&lt;50% of purchase price) and with high-quality development upside.&nbsp; Marvela is currently funded by knowledgeable accredited inventors of the upstream sector, including family offices, Individuals and Traditional GP/Asset Managers.</p>
  <div class="abs about-photo" role="img" aria-label="Rolling green and yellow farmland seen from above"></div>
</section>

<section class="ops">
  <h2 class="abs heading">Operations</h2>
  <p class="abs lead">Marvela is actively leasing in Ohio to execute its lease and drill strategy.</p>
  <div class="abs legend">
    <h3>Legend</h3>
    <ul>
      <li><i style="background:var(--oil)"></i>Oil Window</li>
      <li><i style="background:var(--wet)"></i>Wet Gas Window</li>
      <li><i style="background:var(--dry)"></i>Dry Gas Window</li>
    </ul>
    <div class="scale">
      <svg width="28" height="28" viewBox="0 0 28 28"><circle cx="14" cy="14" r="7" fill="none" stroke="#333" stroke-width="1.5"/><path d="M14 1v26M1 14h26" stroke="#333"/></svg>
      <b></b><span>Miles</span>
    </div>
  </div>
  <div class="abs ops-map" role="img" aria-label="County map of Ohio showing the leasing area: an oil window, a wet gas window and a dry gas window shaded in bands along the eastern counties, from the northeast down to the Ohio River"></div>
</section>

<section class="related">
  <h2 class="abs heading center">Related Entities</h2>
  <div class="abs entity" style="left:108px"><span class="mark">MARVELA</span><span class="sub">Oil and Gas OHIO LLC</span></div>
  <div class="abs entity" style="left:356px"><span class="mark">MARVELA</span><span class="sub">Oil and Gas LLC</span></div>
  <div class="abs entity" style="left:604px"><span class="mark">MARVELA</span><span class="sub">Oil and Gas II LLC</span></div>
  <div class="abs entity" style="left:852px"><span class="mark">MARVELA</span><span class="sub">Minerals LLC</span></div>
</section>

<section class="team">
  <h2 class="abs heading center">Management <span>Team</span></h2>
  <div class="abs person" style="left:113px"><div class="photo" role="img" aria-label="Portrait of the president in a dark suit"></div><h3>Grant Ellison</h3><p>President &amp; CEO</p></div>
  <div class="abs person" style="left:444px"><div class="photo" role="img" aria-label="Portrait of the CFO in a dark suit"></div><h3>Victor Renaldi</h3><p>CFO &amp; Advisor</p></div>
  <div class="abs person" style="left:776px"><div class="photo" role="img" aria-label="Portrait of the vice president of land in a dark suit"></div><h3>Owen Castellano</h3><p>Vice President - Land</p></div>
</section>

<section class="news">
  <h2 class="abs heading center">Latest <span>News</span></h2>
  <article class="abs story" style="left:113px"><div class="photo"><div role="img" aria-label="Drilling rig silhouetted against a sunset sky" style="background:linear-gradient(180deg,#3b6fa8,#9fb2c2 45%,#e6a048 75%,#6a3a1a)"></div></div><h3>New Partnership and<br>Acquisitions</h3><time>02.22.2023</time></article>
  <article class="abs story" style="left:444px"><div class="photo"><div role="img" aria-label="Engineer in a blue hard hat adjusting a valve" style="background:linear-gradient(160deg,#b9c3cc,#7d8a96 40%,#1f3f7a 75%,#2a3540)"></div></div><h3>Oil &amp; Gas Business<br>Licensing</h3><time>04.02.2023</time></article>
  <article class="abs story" style="left:776px"><div class="photo"><div role="img" aria-label="Offshore platform at dusk over the sea" style="background:linear-gradient(180deg,#3d5a7d,#8a9aa8 45%,#3b3a3a 65%,#2d4a66)"></div></div><h3>Marvela is Mining<br>Big Data</h3><time>05.29.2023</time></article>
</section>

<section class="contact">
  <h2 class="abs heading center">Contact <span>Us</span></h2>
  <div class="abs directions">
    <h3>DIRECTIONS</h3>
    <h4>Mailing Address</h4>
    <p>2215 Larkspur Bend Dr #418<br>Houston, Texas 77063</p>
    <h4>Office Address</h4>
    <p>745 Commerce Row Suite 2100<br>Houston, Texas 77002</p>
    <small>Copyright 2023 Marvela Oil &amp; Gas LLC</small>
  </div>
  <form class="abs form">
    <h3>GET IN TOUCH</h3>
    <p class="note">Contact Marvela Royalties by filling out the form below.</p>
    <input class="field" placeholder="Your Name">
    <input class="field" placeholder="Email Address">
    <input class="field" placeholder="Phone">
    <textarea class="field" placeholder="Description of interest"></textarea>
    <button class="submit" type="button">Submit</button>
  </form>
</section>

</body>
</html>
```